Website template for Orvel Sports Massage | ||
Sports & Remedial Therapy | ||
Massage Therapy | ||
It will be www.orvel-sportsmassage.example | ||
We are a professional company, dedicated to providing a natural pain relief from muscular or joint pain/stiffness, using thousands of years old therapy – massage (amongst other techniques e.g. Muscle Energy Technique or Trigger Point Therapy), in a modern fast-paced world where many people seem to be sustaining pain/injury from prolong working with high-tech mobile devices and computers. We relieve stress and muscular pain, increase flexibility within soft tissues and induce relaxation. We treat sports injuries, improve postures, and relieve anxiety/stress through deep tissue massage and other techniques, stretching and prescribed homecare exercises. We work closely and intuitively with soft tissues (muscles, tendons, ligaments, fascia..) and not only treat the current symptoms but also investigate the actual cause of muscular imbalance to encourage optimal healing and rehabilitation. Our clients include city office workers, athletes, manual workers, pregnant clients and everyone else in between. (I will tweak it a bit more but this is what we do in a nutshell.) |
I don’t like bright coloured websites with too many images on Homepage where it takes ages to find stuff. I am looking for a clean look/design which will be really appealing and inviting. I would like to have my logo incorporated and matching colours used. I would like a small picture of me used on the Homepage along with my logo. I'm enclosing a temporary pic of me for the design. Please feel free to use also other images to see different variations... | ||
Cutting-Edge Unique/Creative Professional Futuristic Trendy Friendly Exciting Sophisticated Modern Soft Elegant Service Oriented Fun |
Nice, soft shades of blue (that go well with my logo) | ||
Nice shades of grey (that go well with my logo) | ||
Black or red in subtle doses | ||
Verdana Century Gothic |
top | ||
http://www.brindlebodywork.example | ||
http://www.pelquavent.example/ | ||
http://www.lumaverrespa.example/ | ||
I am open to different ideas and creative input. Many thanks. Additional Information: he navigation details should be as following: Home, Treatments, Prices, Our Therapists, Contact, Testimonials, Shop, FAQS, Careers I would also like a 'join us on Facebook' , 'Buy Gift Vouchers' , 'Specials' and 'Give us your Feedback' quick links somewhere on the Home page. |

```html
<!DOCTYPE html>
<html lang="en">
<head>
<meta charset="utf-8">
<title>Orvel Sports Massage – Sports &amp; Remedial Therapy</title>
<link href="https://fonts.googleapis.com/css2?family=Didact+Gothic&family=Open+Sans:wght@400;600;700&display=swap" rel="stylesheet">
<style>
:root{
  --navy:#1d4f8c;
  --nav-dark:#173f73;
  --blue:#2a6fc4;
  --sky:#8fb9e8;
  --pale:#e6eef8;
  --grey-bg:#dfe3e8;
  --grey:#6b6f74;
  --text:#3a3d40;
  --red:#c4251f;
  --white:#fff;
  --footer:#2b2f35;
}
*{box-sizing:border-box;margin:0;padding:0}
html,body{width:1200px;height:971px;overflow:hidden}
body{background:var(--grey-bg);font-family:"Open Sans",Verdana,sans-serif;color:var(--text);position:relative}
.top-band{position:absolute;left:0;top:0;width:1200px;height:52px;background:linear-gradient(#2c63a8,var(--nav-dark))}
.nav{position:absolute;left:128px;top:0;height:52px;display:flex;list-style:none}
.nav li{height:52px;display:flex;align-items:center;padding:0 19px;color:var(--white);font-size:15px;letter-spacing:.5px;text-transform:uppercase;border-right:1px solid rgba(255,255,255,.25)}
.nav li.active{background:linear-gradient(#7f8792,#555c66)}
.header{position:absolute;left:0;top:52px;width:1200px;height:305px;background:linear-gradient(#f4f6f9,#e3e8ee)}
.header-swoosh{position:absolute;left:0;top:52px}
.brand{position:absolute;left:140px;top:120px;display:flex;align-items:center;gap:14px}
.brand-mark{width:52px;height:52px;border-radius:50%;background:var(--blue)}
.brand-name{font-family:"Didact Gothic",sans-serif;font-size:40px;line-height:1;color:var(--navy);width:260px}
.brand-tag{position:absolute;left:206px;top:225px;font-family:"Didact Gothic",sans-serif;font-size:19px;color:var(--grey)}
.hero-photo{position:absolute;left:430px;top:60px;width:650px;height:270px;background:radial-gradient(ellipse at 45% 45%,#d9cfc8,#b9b1ab 55%,rgba(230,234,240,0) 80%);border-radius:0 0 40px 40px}
.content{position:absolute;left:128px;top:360px;width:952px;height:505px;background:var(--white)}
.welcome{position:absolute;left:22px;top:18px;width:460px}
.welcome h1{font-family:"Didact Gothic",sans-serif;font-weight:400;font-size:25px;color:var(--text)}
.welcome h1 span{color:var(--blue)}
.welcome .sub{font-family:"Didact Gothic",sans-serif;font-size:13px;color:var(--grey);margin-top:2px}
.intro{position:absolute;left:22px;top:82px;width:730px;font-size:11.3px;line-height:19.3px;color:var(--text)}
.portrait{position:absolute;left:478px;top:82px;width:150px;height:190px;background:linear-gradient(#eceff2,#c9ccd0);border:1px solid #ddd;float:right}
.therapy{position:absolute;left:22px;top:355px;width:420px}
.therapy h2{font-family:"Didact Gothic",sans-serif;font-weight:400;font-size:21px;color:var(--text);margin-bottom:6px}
.therapy li{list-style:none;font-size:11.5px;line-height:25px;padding-left:18px;position:relative;border-bottom:1px dotted #ccc}
.therapy li::before{content:"";position:absolute;left:3px;top:9px;width:7px;height:7px;border-radius:50%;background:var(--blue)}
.voucher{position:absolute;left:445px;top:360px;width:225px;height:105px;background:linear-gradient(#f4f7fb,#dbe5f2);border:1px solid #c8d4e3;border-radius:4px}
.voucher h3{position:absolute;left:12px;top:10px;font-family:"Didact Gothic",sans-serif;font-size:21px;line-height:23px;font-weight:400;color:var(--red)}
.voucher .art{position:absolute;right:10px;top:14px;width:95px;height:70px;background:linear-gradient(135deg,#f3c8d6,#c9ddf3);border-radius:4px}
.voucher .btn{position:absolute;left:12px;top:68px;background:#222;color:#fff;font-size:11px;padding:4px 12px;border-radius:10px}
.sidebar{position:absolute;left:732px;top:10px;width:205px}
.feedback-tab{height:40px;border-radius:6px;background:linear-gradient(#4b86cf,var(--navy));display:flex;align-items:center;gap:10px;padding-left:12px;color:#fff;font-family:"Didact Gothic",sans-serif;font-size:17px}
.feedback-tab i{width:20px;height:20px;border-radius:4px;background:#f2c14a}
.form{padding:10px 0 0}
.form label{display:block;font-size:10px;color:var(--grey);margin-top:6px}
.form .field{height:20px;border:1px solid #bcc4cd;background:#f7f9fb}
.form .area{height:44px}
.submit{margin:8px 0 0 95px;width:80px;height:20px;background:#222;color:#fff;font-size:10px;display:flex;align-items:center;justify-content:center;border-radius:10px;font-weight:700}
.appoint{margin-top:16px;height:78px;border-radius:5px;background:linear-gradient(var(--blue),var(--nav-dark));color:#fff;position:relative;padding:10px 0 0 10px;font-size:12px;line-height:15px}
.appoint strong{display:block;font-size:17px;margin-top:4px}
.appoint .clock{position:absolute;right:8px;top:10px;width:58px;height:58px;border-radius:50%;background:linear-gradient(#f3f3f3,#a9b0b8)}
.special{margin-top:12px;height:88px;border-radius:5px;background:linear-gradient(#8d9399,#4f545a);color:#fff;position:relative;padding:14px 0 0 12px;font-size:14px}
.special strong{font-size:22px;color:#fff}
.special em{display:block;font-style:normal;color:#ffd2cf;font-size:14px;margin-top:2px}
.special .badge{position:absolute;right:-4px;top:-10px;width:62px;height:62px;border-radius:50%;background:var(--red);color:#fff;display:flex;align-items:center;justify-content:center;font-size:11px;transform:rotate(-20deg)}
.footer{position:absolute;left:0;top:880px;width:1200px;height:91px;background:linear-gradient(#3c4249,var(--footer))}
.foot-brand{position:absolute;left:140px;top:20px;font-family:"Didact Gothic",sans-serif;color:#fff;font-size:21px;line-height:22px;width:130px}
.foot-links{position:absolute;left:250px;top:20px;font-size:11px;color:#dfe4ea;word-spacing:2px}
.foot-copy{position:absolute;left:250px;top:40px;font-size:11px;color:#b9c0c8}
.social{position:absolute;left:905px;top:24px;display:flex;gap:18px}
.social i{width:26px;height:26px;border-radius:4px;background:#4d79b3}
</style>
</head>
<body>
<div class="top-band"></div>
<ul class="nav">
  <li class="active">Home</li><li>Treatments</li><li>Prices</li><li>Our Therapists</li><li>Contact</li><li>Testimonials</li><li>Shop</li><li>FAQs</li><li>Careers</li>
</ul>

<div class="header"></div>
<svg class="header-swoosh" width="1200" height="305" viewBox="0 0 1200 305" aria-hidden="true">
  <path d="M128 250 Q600 330 1080 245 L1080 305 L128 305Z" fill="#3a76c4"/>
  <path d="M128 262 Q600 330 1080 258" stroke="#9cc2ee" stroke-width="4" fill="none"/>
  <path d="M0 285 Q600 320 1200 270" stroke="#c8d6e6" stroke-width="2" fill="none"/>
</svg>
<div class="brand"><span class="brand-mark"></span><span class="brand-name">Orvel Sports Massage</span></div>
<div class="brand-tag">Sports &amp; Remedial Therapy</div>
<div class="hero-photo" role="img" aria-label="Photo collage of bare backs and shoulders receiving massage, with pain points highlighted"></div>

<main class="content">
  <div class="welcome">
    <h1>Welcome to <span>Orvel Sports Massage</span></h1>
    <p class="sub">Sport &amp; Remedial Therapy</p>
  </div>
  <p class="intro" style="width:450px">We are a professional company, dedicated to providing a natural pain relief from muscular or joint pain/stiffness, using thousands of years old therapy – massage (amongst other techniques e.g. Muscle Energy Technique or Trigger Point Therapy), in a modern fast-paced world where many people seem to be sustaining pain/injury from prolong working with high-tech mobile devices and computers. We relieve stress and muscular pain, increase flexibility within soft tissues and induce relaxation. We treat sports injuries, improve postures, and relieve anxiety/stress through deep tissue massage and other techniques, stretching and prescribed homecare exercises. We work closely and intuitively with soft tissues (muscles, tendons, ligaments, fascia..) and not only treat the current symptoms but also investigate the actual cause of muscular imbalance to encourage optimal healing and rehabilitation. Our clients include city office workers, athletes, manual workers, pregnant clients and everyone else in between.</p>
  <div class="portrait" role="img" aria-label="Portrait photo of the therapist"></div>

  <section class="therapy">
    <h2>Our Therapy</h2>
    <ul>
      <li>Nam vel massa at erat pellentesque lobortis.</li>
      <li>Etiam convallis mollis diam, ut lobortis dolor consequat id.</li>
      <li>Aliquam convallis varius leo, sed feugiat augue portsin.</li>
      <li>Phasellus eget mauris non elit blandit scelerisque a ac turpis.</li>
    </ul>
  </section>

  <div class="voucher">
    <h3>Buy Gift<br>Vouchers</h3>
    <div class="art" role="img" aria-label="Illustration of a wrapped gift voucher"></div>
    <span class="btn">Click here</span>
  </div>

  <aside class="sidebar">
    <div class="feedback-tab"><i></i>Your Feedback</div>
    <div class="form">
      <label>Name:</label><div class="field"></div>
      <label>Email:</label><div class="field"></div>
      <label>Phone:</label><div class="field"></div>
      <label>Question/Comments:</label><div class="field area"></div>
      <div class="submit">SUBMIT</div>
    </div>
    <div class="appoint">Get Appointment<br>Now Call us at<strong>123-456-7890</strong>
      <span class="clock" role="img" aria-label="Illustration of a wall clock"></span></div>
    <div class="special">Get <strong>$10</strong> off<em>for every Referral</em><span class="badge">Special</span></div>
  </aside>
</main>

<footer class="footer">
  <div class="foot-brand">Orvel Sports Massage</div>
  <div class="foot-links">Home | Treatments | Prices | Our Therapists | Contact | Testimonials | Shop | FAQS | Careers</div>
  <div class="foot-copy">Copyright © <b>Orvel Sports Massage</b>, All right reserved.</div>
  <div class="social"><i></i><i></i><i></i><i></i></div>
</footer>
</body>
</html>
```